Church Invite (Business Sized)

I would like to get a design for a church invite card. The design should be able to be used on business sized cards. The front should include the "Beacon" logo provided with the phrase "You're Welcomed Here". The back should include the church logo, name, address, phone number, and website.

Church Name: Evergreen Harvest Fellowship
Church Address: 1847 Willow Lane, Decatur, GA, 30871
Church Number: 555-283-1947
Church Website: www.ehfchurchhome.org

```html
<!DOCTYPE html>
<html lang="en">
<head>
<meta charset="utf-8">
<title>Evergreen Harvest Fellowship – Card Back</title>
<link rel="stylesheet" href="https://fonts.googleapis.com/css2?family=Figtree:wght@300;400;700&display=swap">
<style>
  :root {
    --brand-blue: #1b64ae;
    --brand-cyan: #0db0d5;
    --deep-blue: #0a609f;
    --paper: #ffffff;
    --contact-text: #ffffff;
  }
  * { margin: 0; padding: 0; box-sizing: border-box; }
  html, body { width: 1200px; height: 726px; overflow: hidden; background: var(--paper); }
  .card {
    position: relative;
    width: 1200px;
    height: 726px;
    background: var(--paper);
    font-family: "Figtree", sans-serif;
    overflow: hidden;
  }
  .website {
    position: absolute;
    right: 60px;
    top: 38px;
    font-size: 38px;
    font-weight: 400;
    line-height: 1;
    color: var(--brand-cyan);
  }
  .brand-mark {
    position: absolute;
    left: 136px;
    top: 210px;
    width: 160px;
    height: 160px;
    background: var(--brand-blue);
  }
  .church-name {
    color: var(--brand-blue);
    font-weight: 400;
  }
  .church-name span {
    position: absolute;
    left: 398px;
    line-height: 1;
    white-space: nowrap;
  }
  .church-name .line-one { top: 222px; font-size: 64px; font-weight: 700; }
  .church-name .line-two { top: 296px; font-size: 60px; font-weight: 300; }
  .backdrop-art {
    position: absolute;
    left: 148px;
    top: 474px;
    width: 1052px;
    height: 252px;
    background: linear-gradient(100deg, var(--brand-cyan) 0%, var(--brand-blue) 35%, var(--deep-blue) 70%, var(--brand-cyan) 100%);
  }
  .contact {
    position: absolute;
    left: 468px;
    color: var(--contact-text);
    font-size: 37px;
    font-weight: 300;
    line-height: 1;
    display: flex;
    align-items: center;
    gap: 18px;
    white-space: nowrap;
  }
  .contact svg { width: 30px; height: 38px; flex: none; }
  .contact-phone { top: 592px; }
  .contact-address { top: 660px; }
</style>
</head>
<body>
<main class="card">
  <p class="website">www.ehfchurchhome.org</p>

  <div class="brand-mark" aria-hidden="true"></div>
  <h1 class="church-name">
    <span class="line-one">Evergreen</span>
    <span class="line-two">Harvest Fellowship</span>
  </h1>

  <div class="backdrop-art" role="img" aria-label="Decorative layered blue and cyan mountain shapes"></div>

  <p class="contact contact-phone">
    <svg viewBox="0 0 30 38" aria-hidden="true">
      <rect x="6" y="2" width="18" height="34" rx="3" fill="none" stroke="#fff" stroke-width="2.5"/>
      <line x1="6" y1="8" x2="24" y2="8" stroke="#fff" stroke-width="2"/>
      <line x1="6" y1="29" x2="24" y2="29" stroke="#fff" stroke-width="2"/>
      <circle cx="15" cy="32.5" r="1.5" fill="#fff"/>
    </svg>
    <span>555-283-1947</span>
  </p>
  <p class="contact contact-address">
    <svg viewBox="0 0 30 38" aria-hidden="true">
      <path d="M15 2C8.4 2 4 7 4 13c0 8 11 22 11 22s11-14 11-22C26 7 21.6 2 15 2z" fill="#fff"/>
      <circle cx="15" cy="13" r="4.2" fill="var(--deep-blue)"/>
    </svg>
    <span>1847 Willow Lane, Decatur, GA, 30871</span>
  </p>
</main>
</body>
</html>
```